Billboard Design for Equipment Rental Business

We need a billboard design for our equipment rental business called Brindlewood Equipment Company. We are based in Georgia. We rent construction tools, equipment, and dumpsters. We currently have a design but feel like we could get something better. Our phone number is 912-730-2591 and our website is www.brindlewoodequipment-example.com

```html
<!DOCTYPE html>
<html lang="en">
<head>
<meta charset="utf-8">
<title>Brindlewood Equipment Company – Billboard</title>
<link href="https://fonts.googleapis.com/css2?family=Archivo+Black&family=Oswald:wght@500;600&family=Roboto+Condensed:wght@700&display=swap" rel="stylesheet">
<style>
  :root {
    --page: #d6d6d6;
    --ink: #1c1a17;
    --safety: #f6bd22;
    --safety-deep: #e9af1c;
    --rule: rgba(28, 26, 23, 0.55);
  }
  html, body {
    margin: 0;
    width: 1000px;
    height: 1200px;
    overflow: hidden;
    background: var(--page);
  }
  .billboard {
    position: absolute;
    left: 40px;
    top: 357px;
    width: 920px;
    height: 486px;
    box-sizing: border-box;
    padding: 26px;
    background: repeating-linear-gradient(-45deg, var(--ink) 0 14px, var(--safety) 14px 28px);
    box-shadow: 0 14px 30px rgba(0,0,0,0.25);
  }
  .board-face {
    position: relative;
    width: 100%;
    height: 100%;
    background: repeating-linear-gradient(-60deg, var(--safety) 0 20px, var(--safety-deep) 20px 40px);
    color: var(--ink);
    white-space: nowrap;
  }
  .brand {
    position: absolute;
    left: 50px;
    right: 50px;
    top: 52px;
    display: flex;
    align-items: center;
    gap: 26px;
  }
  .brand-mark {
    flex: none;
    width: 74px;
    height: 74px;
    background: var(--ink);
  }
  .brand-text { flex: 1; }
  .brand-name {
    margin: 0;
    font-family: "Archivo Black", sans-serif;
    font-size: 70px;
    line-height: 0.95;
    letter-spacing: -1px;
  }
  .brand-tagline {
    margin: 10px 0 0 4px;
    font-family: "Oswald", sans-serif;
    font-weight: 500;
    font-size: 30px;
    line-height: 1.1;
    letter-spacing: 7px;
  }
  .divider {
    position: absolute;
    left: 42px;
    right: 42px;
    height: 1px;
    background: var(--rule);
  }
  .divider--top { top: 246px; }
  .divider--bottom { top: 320px; }
  .services {
    position: absolute;
    left: 42px;
    right: 42px;
    top: 252px;
    height: 62px;
    display: flex;
    align-items: center;
    justify-content: space-between;
    font-family: "Oswald", sans-serif;
    font-weight: 500;
    font-size: 34px;
    line-height: 1;
    text-transform: uppercase;
  }
  .service { display: flex; align-items: center; gap: 12px; }
  .service svg, .contact svg { width: 30px; height: 30px; flex: none; }
  .slash { font-family: "Oswald", sans-serif; font-weight: 500; font-size: 38px; line-height: 1; }
  .contact {
    position: absolute;
    left: 42px;
    right: 42px;
    top: 334px;
    height: 72px;
    display: flex;
    align-items: center;
    gap: 22px;
  }
  .phone {
    display: flex;
    align-items: center;
    gap: 12px;
    font-family: "Oswald", sans-serif;
    font-weight: 600;
    font-size: 48px;
    line-height: 1;
  }
  .contact .slash { margin-left: auto; }
  .website {
    font-family: "Roboto Condensed", sans-serif;
    font-weight: 700;
    font-size: 21px;
    line-height: 1;
  }
</style>
</head>
<body>
  <section class="billboard" aria-label="Brindlewood Equipment Company billboard">
    <div class="board-face">
      <header class="brand">
        <div class="brand-mark"></div>
        <div class="brand-text">
          <h1 class="brand-name">BRINDLEWOOD</h1>
          <p class="brand-tagline">EQUIPMENT COMPANY</p>
        </div>
      </header>

      <div class="divider divider--top"></div>
      <nav class="services">
        <span class="service">
          <svg viewBox="0 0 30 30" fill="none" stroke="currentColor" stroke-width="2.2" stroke-linecap="round">
            <line x1="5" y1="5" x2="25" y2="25"/><line x1="25" y1="5" x2="5" y2="25"/>
            <circle cx="5" cy="25" r="3"/><circle cx="25" cy="5" r="3"/>
          </svg>Tools</span>
        <span class="slash">/</span>
        <span class="service">
          <svg viewBox="0 0 30 30" fill="none" stroke="currentColor" stroke-width="2.2" stroke-linejoin="round">
            <rect x="4" y="10" width="22" height="12"/><line x1="4" y1="26" x2="26" y2="26"/>
          </svg>Equipment</span>
        <span class="slash">/</span>
        <span class="service">
          <svg viewBox="0 0 30 30" fill="none" stroke="currentColor" stroke-width="2.2" stroke-linejoin="round">
            <path d="M4 9 H26 L24 25 H6 Z"/><line x1="11" y1="12" x2="11" y2="22"/><line x1="15" y1="12" x2="15" y2="22"/><line x1="19" y1="12" x2="19" y2="22"/><line x1="3" y1="6" x2="27" y2="6"/>
          </svg>Dumpsters</span>
      </nav>
      <div class="divider divider--bottom"></div>

      <footer class="contact">
        <span class="phone">
          <svg viewBox="0 0 30 30" fill="none" stroke="currentColor" stroke-width="2.2" stroke-linejoin="round">
            <path d="M7 4 L11 4 L13 10 L10 12 C12 17 14 19 19 21 L21 18 L27 20 L27 24 C27 26 25 27 23 27 C13 26 5 18 4 8 C4 6 5 4 7 4 Z"/>
          </svg>912-730-2591</span>
        <span class="slash">/</span>
        <span class="website">www.brindlewoodequipment-example.com</span>
      </footer>
    </div>
  </section>
</body>
</html>
```